Quiet Harbor Roasters - Full Brand Packaging Suite (Pods, Boxes, Bags)

Quiet Harbor Roasters is commissioning a complete packaging system for our 12‑roast specialty coffee collection. Each roast is inspired by a Christian ministry, and every package must follow a consistent storytelling structure across all formats: single‑serve pod lids, 12‑count and 24‑count pod boxes, 12 oz bags, and 2 lb bags.Packaging Formats Needed:• Single‑Serve Pod Lids: Circular design featuring roast name, roast type, ministry inspiration, and color theme.
• 12‑Count & 24‑Count Pod Boxes: Full panel design (front, back, sides, top) matching the roast’s identity and ministry story.
• 12 oz Bag: Vertical layout with strong shelf presence, roast color theme, ministry spotlight, and brand story.
• 2 lb Bag: Same design language as the 12 oz bag, scaled appropriately.
Required Panel Structure (applies to every roast):• Front Panel:• Roast Name
• Roast Type
• “Inspired By: [Open Fields Ministries]”
• “Mission Driven | Fueling Global Impact”
• “Brew it. Share it. Fuel the Mission.”

• Side A — Roast Story:
A short, emotionally resonant description connecting the roast’s flavor profile or theme to the ministry’s impact.
• Side B — Ministry Spotlight:
Open Fields Ministries, mission summary, and a “Scan to Give” callout with website link.
• Back Panel:• Flavor Notes
• Origin
• Quiet Harbor Roasters Story (provided text stays consistent across all roasts)
• Statement of giving: “50% of net proceeds support our ministry partners + 10% of gross sales from each roast go directly to the ministry it represents.”

Brand Identity:
Quiet Harbor Roasters blends premium specialty coffee with faith‑driven purpose. Designs should feel clean, premium, unified, and visually distinct per roast through color, tone, and ministry theme.Deliverables:• Print‑ready files for all packaging formats
• Editable source files
• Cohesive color system across all 12 roasts
• Consistent layout structure across lids, boxes, and bags
Goal:
Create a unified, premium packaging system that elevates each roast’s identity, communicates its ministry partnership, and strengthens the mission‑driven heart of Quiet Harbor Roasters.

Target Market(s)

Churches

Industry/Entity Type

Churches, ministries, Christian’s

Requirements
Must have
• I’d like the design to look like the AI GENERATED image I had made of the packaging. It looks classy and clean.
Should not have
• Colorful palette, silly pictures, cartons, mascots

```html
<!DOCTYPE html>
<html lang="en">
<head>
<meta charset="UTF-8">
<title>Quiet Harbor Roasters – Steadfast Dawn 12 oz Bag Front</title>
<link rel="stylesheet" href="https://fonts.googleapis.com/css2?family=Oswald:wght@400;600&family=Playfair+Display:wght@600&family=Libre+Caslon+Text&display=swap">
<style>
  :root {
    --backdrop: #e2e2e2;
    --bag-black: #151515;
    --bag-black-soft: #222222;
    --silver: #b9b9b9;
    --muted-grey: #8d8d8d;
    --white: #f4f4f4;
    --gold-light: #e4c15a;
    --gold: #c99a2c;
    --gold-deep: #9c7320;
  }
  * { margin: 0; padding: 0; box-sizing: border-box; }
  html, body {
    width: 1200px;
    height: 1200px;
    overflow: hidden;
    background: var(--backdrop);
  }
  .canvas {
    position: relative;
    width: 1200px;
    height: 1200px;
  }
  .bag-front {
    position: absolute;
    left: 290px;
    top: 70px;
    width: 620px;
    height: 1060px;
    background: linear-gradient(160deg, var(--bag-black-soft) 0%, var(--bag-black) 55%, #101010 100%);
    text-align: center;
  }
  .bag-front > * {
    position: absolute;
    left: 0;
    right: 0;
  }
  .brand-mark {
    top: 120px;
    display: flex;
    align-items: center;
    justify-content: center;
    gap: 18px;
    font-family: "Oswald", sans-serif;
    font-weight: 600;
    color: var(--silver);
    text-transform: uppercase;
  }
  .brand-mark__dot {
    width: 44px;
    height: 44px;
    border-radius: 50%;
    background: var(--silver);
    flex: none;
  }
  .brand-mark__name {
    font-size: 54px;
    line-height: 1.02;
    letter-spacing: 2px;
    text-align: left;
  }
  .roast-name {
    top: 440px;
    font-family: "Playfair Display", serif;
    font-weight: 600;
    font-size: 74px;
    line-height: 1.12;
    letter-spacing: 2px;
    text-transform: uppercase;
    background: linear-gradient(100deg, var(--gold-deep) 0%, var(--gold-light) 35%, var(--gold) 65%, var(--gold-deep) 100%);
    -webkit-background-clip: text;
    background-clip: text;
    color: transparent;
  }
  .roast-subtitle {
    top: 622px;
    font-family: "Libre Caslon Text", serif;
    font-size: 22px;
    letter-spacing: 3px;
    color: var(--white);
    text-transform: uppercase;
  }
  .gold-rule {
    top: 690px;
    left: 90px;
    right: 90px;
    height: 4px;
    background: linear-gradient(90deg, var(--gold-deep), var(--gold-light), var(--gold));
  }
  .info-line {
    font-family: "Oswald", sans-serif;
    font-weight: 400;
    font-size: 20px;
    letter-spacing: 2.5px;
    color: var(--muted-grey);
    text-transform: uppercase;
  }
  .roast-details { top: 735px; }
  .ministry-credit { top: 790px; color: var(--silver); }
  .mission-line { top: 828px; }
  .brew-line { top: 915px; color: var(--gold); }
  .tagline { top: 955px; }
</style>
</head>
<body>
  <main class="canvas">
    <section class="bag-front">
      <div class="brand-mark">
        <span class="brand-mark__dot" aria-hidden="true"></span>
        <span class="brand-mark__name">Quiet Harbor<br>Roasters</span>
      </div>
      <h1 class="roast-name">Steadfast<br>Dawn</h1>
      <p class="roast-subtitle">Premium Single Origin</p>
      <div class="gold-rule" aria-hidden="true"></div>
      <p class="info-line roast-details">Dark Roast | Net Wt. 12 oz (340g)</p>
      <p class="info-line ministry-credit">Inspired By: Open Fields Ministries</p>
      <p class="info-line mission-line">Mission Driven | Fueling Global Impact</p>
      <p class="info-line brew-line">Brew it. Share it. Fuel the Mission.</p>
      <p class="info-line tagline">Born of Faith. Roasted for Purpose</p>
    </section>
  </main>
</body>
</html>
```